I need a business Card Design for my practice , i am clinical herbalist. I am a herbalist specializing in Lyme disease, autism, autoimmune diseases, difficult to cure diseasesDifficult to cure diseases. In my innovative practice i link traditional medicine, herbs with science, immunologu ,pharmacology.

Industry/Entity Type

Business

Contact Information for Business Card

My company name : OŚRODEK ZIELNIK
My name : Piotr Kaleta
Name of my profession : Fitoterapeuta
In Polish language Fitoterapeuta is Herbalist .

e-mail: piotrkaleta@osrodekzielnik.com
www.osrodek-zielnik.pl
phone : 604 587 231
My company adress : Dąbrowa Sitnicka 41 , 38-415 Lużna
I dont have logo .

Requirements
Nice to have
• My company

```html
<!DOCTYPE html>
<html lang="pl">
<head>
<meta charset="utf-8">
<title>Ośrodek Zielnik – wizytówka</title>
<link rel="stylesheet" href="https://fonts.googleapis.com/css2?family=Montserrat:wght@400;500;700&family=Exo+2:wght@700&display=swap">
<style>
  :root {
    --page-bg: #f1efeb;
    --card-bg: #e8e5df;
    --card-edge: #d6d2ca;
    --brand-green: #2f8a34;
    --text-green: #3f8a3c;
    --text-grey: #4f4f4f;
    --text-dark: #3a3a3a;
    --art-light: #dcded6;
    --art-mid: #b9cdb4;
  }
  html, body {
    margin: 0;
    padding: 0;
    width: 1200px;
    height: 1000px;
    overflow: hidden;
    background: var(--page-bg);
  }
  .canvas {
    position: relative;
    width: 1200px;
    height: 1000px;
  }
  .business-card {
    position: absolute;
    left: 150px;
    top: 268px;
    width: 945px;
    height: 512px;
    border-radius: 16px;
    background: var(--card-bg);
    box-shadow: 0 0 0 1px var(--card-edge);
    overflow: hidden;
    font-family: "Montserrat", sans-serif;
  }
  .green-panel {
    position: absolute;
    inset: 0;
  }
  .leaf-art {
    position: absolute;
    left: 690px;
    top: 200px;
    width: 250px;
    height: 312px;
    border-radius: 14px 14px 0 0;
    background: linear-gradient(160deg, var(--art-light) 0%, var(--art-mid) 100%);
  }
  .company-name {
    position: absolute;
    left: 48px;
    top: 88px;
    margin: 0;
    font-size: 34px;
    font-weight: 700;
    color: var(--text-green);
    letter-spacing: 1px;
  }
  .person-name {
    position: absolute;
    left: 48px;
    top: 184px;
    margin: 0;
    font-family: "Exo 2", sans-serif;
    font-size: 32px;
    font-weight: 700;
    color: var(--text-green);
    letter-spacing: 0.8px;
  }
  .person-role {
    position: absolute;
    left: 48px;
    top: 221px;
    margin: 0;
    font-size: 20px;
    font-weight: 500;
    color: var(--text-grey);
    letter-spacing: 0.5px;
  }
  .contact-list {
    position: absolute;
    left: 48px;
    top: 302px;
    margin: 0;
    padding: 0;
    list-style: none;
    font-size: 18px;
    letter-spacing: 0.5px;
    color: var(--text-dark);
  }
  .contact-address { margin-bottom: 12px; line-height: 24px; }
  .contact-address .icon { display: block; margin: 0 0 6px 2px; }
  .contact-row {
    display: flex;
    align-items: center;
    gap: 14px;
    height: 26px;
  }
  .icon { width: 16px; height: 16px; fill: var(--brand-green); flex: none; }
  .web-domain { color: var(--text-green); }
</style>
</head>
<body>
<main class="canvas">
  <section class="business-card">
    <svg class="green-panel" width="945" height="512" viewBox="0 0 945 512" aria-hidden="true">
      <path d="M545 0 Q755 256 547 512 L945 512 L945 0 Z" fill="var(--brand-green)"/>
    </svg>
    <div class="leaf-art" role="img" aria-label="Ilustracja liścia z żyłkami"></div>

    <h1 class="company-name">OŚRODEK ZIELNIK</h1>
    <h2 class="person-name">PIOTR KALETA</h2>
    <p class="person-role">Fitoterapeuta</p>

    <ul class="contact-list">
      <li class="contact-address">
        <svg class="icon" viewBox="0 0 16 16" aria-hidden="true"><path d="M1 12 L15 2 L9 15 L8 10 Z" fill="none" stroke="var(--brand-green)" stroke-width="1.4" stroke-linejoin="round"/></svg>
        Dąbrowa Sitnicka 41,<br>38-415 Lużna
      </li>
      <li class="contact-row">
        <svg class="icon" viewBox="0 0 16 16" aria-hidden="true"><path d="M3.5 1.5 L6 1 L7.5 4.5 L5.8 5.8 C6.6 7.8 8.2 9.4 10.2 10.2 L11.5 8.5 L15 10 L14.5 12.5 C14.2 14 13 14.8 11.5 14.5 C6.5 13.5 2.5 9.5 1.5 4.5 C1.2 3 2 1.8 3.5 1.5 Z"/></svg>
        <span>604 587 231</span>
      </li>
      <li class="contact-row">
        <svg class="icon" viewBox="0 0 16 16" aria-hidden="true"><rect x="1" y="3" width="14" height="10" rx="1"/><path d="M1.5 3.8 L8 9 L14.5 3.8" fill="none" stroke="var(--card-bg)" stroke-width="1.3"/></svg>
        <span>piotrkaleta@osrodekzielnik.com</span>
      </li>
      <li class="contact-row">
        <svg class="icon" viewBox="0 0 16 16" aria-hidden="true"><circle cx="9.5" cy="6.5" r="4.8" fill="none" stroke="var(--brand-green)" stroke-width="1.8"/><path d="M6 10 L1.5 14.5" stroke="var(--brand-green)" stroke-width="2.2" stroke-linecap="round"/></svg>
        <span>www.<span class="web-domain">osrodek-zielnik</span>.pl</span>
      </li>
    </ul>
  </section>
</main>
</body>
</html>
```